Marine Business Card

We install Lighting, Sound, Video, PA Systems to hotels, nightclubs, Restaurants, Cruise Ships.

Target Market(s)

We want to focus on the Marine or Maritime/Cruise industry. Passenger ships and cruise liners are the companies we want to appeal to

Industry/Entity Type

Business

Contact Information for Business Card

Mark Dellow
Managing Director
Harbourne Beam and Audio Marine Ltd

Requirements
Must have
• Office: 01632 960418
Mobile: 07700 900371
mark@harbournebeamandaudio.co.uk
www.harbournebeamandaudio.co.uk

```html
<!DOCTYPE html>
<html lang="en">
<head>
<meta charset="utf-8">
<title>Mark Dellow – Business Card</title>
<link href="https://fonts.googleapis.com/css2?family=Open+Sans:wght@300;400;600;700&family=Teko:wght@400&family=Inter:wght@700&display=swap" rel="stylesheet">
<style>
  :root {
    --canvas-bg: #e9e9e9;
    --card-white: #ffffff;
    --blue-light: #6fb5fb;
    --blue-deep: #005b96;
    --ink: #222222;
    --ink-soft: #444444;
    --text-light: #ffffff;
    --ship-tone-a: #555555;
    --ship-tone-b: #1e1e1e;
    --card-shadow: 8px 8px 14px rgba(0, 0, 0, 0.18);
  }
  * { margin: 0; padding: 0; box-sizing: border-box; }
  html, body {
    width: 1200px;
    height: 1000px;
    overflow: hidden;
    background: var(--canvas-bg);
  }
  .canvas { position: relative; width: 1200px; height: 1000px; }

  .card {
    position: absolute;
    width: 532px;
    height: 307px;
    border-radius: 22px;
    box-shadow: var(--card-shadow);
  }

  /* Front */
  .card-front {
    left: 347px;
    top: 146px;
    background: linear-gradient(135deg, var(--blue-light) 12%, #3d8fd3 45%, var(--blue-deep) 80%);
    color: var(--text-light);
  }
  .front-name {
    position: absolute;
    left: 51px;
    top: 186px;
    font-family: "Inter", Arial, sans-serif;
    font-weight: 700;
    font-size: 26px;
    letter-spacing: -1px;
    line-height: 1;
  }
  .front-contact {
    position: absolute;
    left: 251px;
    top: 188px;
    font-family: "Open Sans", Arial, sans-serif;
    font-size: 14.5px;
    line-height: 18px;
  }
  .front-contact .phones { font-weight: 400; margin-bottom: 6px; }
  .front-contact .phones b { font-weight: 700; }
  .front-contact .phones .gap { display: inline-block; width: 8px; }
  .front-contact .web { font-weight: 300; }

  /* Back */
  .card-back {
    left: 344px;
    top: 531px;
    background: var(--card-white);
    text-align: center;
  }
  .ship-illustration {
    position: absolute;
    left: 181px;
    top: 100px;
  }
  .back-name {
    position: absolute;
    left: 0;
    width: 100%;
    top: 172px;
    font-family: "Teko", "Arial Narrow", sans-serif;
    font-weight: 400;
    font-size: 34px;
    letter-spacing: 7px;
    line-height: 1;
    color: var(--ink);
    padding-left: 7px;
  }
  .back-role {
    position: absolute;
    left: 0;
    width: 100%;
    top: 205px;
    font-family: "Open Sans", Arial, sans-serif;
    font-weight: 700;
    font-size: 12px;
    color: var(--ink-soft);
  }
  .back-company {
    position: absolute;
    left: 0;
    width: 100%;
    top: 221px;
    font-family: "Open Sans", Arial, sans-serif;
    font-weight: 300;
    font-size: 11px;
    letter-spacing: -0.3px;
    color: var(--ink);
  }
</style>
</head>
<body>
<div class="canvas">

  <section class="card card-front">
    <div class="front-name">Mark Dellow</div>
    <div class="front-contact">
      <div class="phones"><b>o</b> 01632.960.418<span class="gap"></span><b>m</b> 07700.900.371</div>
      <div class="web">mark@harbournebeamandaudio.co.uk</div>
      <div class="web">www.harbournebeamandaudio.co.uk</div>
    </div>
  </section>

  <section class="card card-back">
    <svg class="ship-illustration" width="175" height="60" viewBox="0 0 175 60" role="img" aria-label="Cruise yacht silhouette illustration">
      <defs>
        <linearGradient id="shipTone" x1="0" y1="0" x2="1" y2="1">
          <stop offset="0" stop-color="var(--ship-tone-a)"/>
          <stop offset="1" stop-color="var(--ship-tone-b)"/>
        </linearGradient>
      </defs>
      <rect x="0" y="0" width="175" height="60" rx="6" fill="url(#shipTone)"/>
    </svg>
    <div class="back-name">MARK DELLOW</div>
    <div class="back-role">Managing Director</div>
    <div class="back-company">Harbourne Beam and Audio Marine Ltd</div>
  </section>

</div>
</body>
</html>
```